Roaming outings business card

please see website
www.roamingoutings.comau

info needed on card
Keiran Voss
Ph
email
Adventure Riding GPS trails

please use my logo and colours off my site

Business

Keiran Voss
keiran@roamingoutings.com

```html
<!DOCTYPE html>
<html lang="en">
<head>
<meta charset="utf-8">
<title>Roaming Outings – Business Card</title>
<link rel="stylesheet" href="https://fonts.googleapis.com/css2?family=PT+Sans:ital,wght@0,400;0,700;1,400&display=swap">
<style>
  :root {
    --card-bg: #ffffff;
    --ink: #1a1a1a;
    --brand-dark: #1f1f1f;
    --brand-yellow: #f3d21c;
    --link-gold: #d8aa12;
    --icon-grey: #3a3a3a;
    --rider-dark: #2a2a2a;
    --rider-light: #8a8a8a;
  }
  * { margin: 0; padding: 0; box-sizing: border-box; }
  html, body {
    width: 1200px;
    height: 702px;
    overflow: hidden;
    background: var(--card-bg);
  }
  .card {
    position: relative;
    width: 1200px;
    height: 702px;
    background: var(--card-bg);
    font-family: "PT Sans", sans-serif;
    color: var(--ink);
  }
  .brand-mark {
    position: absolute;
    left: 92px;
    top: 104px;
    width: 150px;
    height: 150px;
    border-radius: 50%;
    background: var(--brand-yellow);
  }
  .brand-name {
    position: absolute;
    left: 306px;
    top: 116px;
    font-weight: 700;
    font-size: 58px;
    line-height: 64px;
    letter-spacing: 1px;
    text-transform: uppercase;
    color: var(--brand-dark);
  }
  .tagline {
    position: absolute;
    left: 270px;
    top: 256px;
    font-style: italic;
    font-size: 34px;
    color: var(--ink);
  }
  .rider-illustration {
    position: absolute;
    left: 738px;
    top: 268px;
    width: 374px;
    height: 366px;
    border-radius: 46% 40% 42% 42%;
    background: radial-gradient(ellipse at 55% 45%, var(--rider-dark) 0%, #555 55%, #cfcfcf 100%);
    opacity: 0.85;
  }
  .contact {
    position: absolute;
    left: 82px;
    top: 428px;
  }
  .contact-name {
    font-weight: 700;
    font-size: 41px;
    line-height: 52px;
    margin-bottom: 8px;
  }
  .contact-list { list-style: none; }
  .contact-item {
    display: flex;
    align-items: center;
    font-size: 37px;
    line-height: 48px;
  }
  .contact-icon {
    width: 30px;
    height: 30px;
    margin-right: 18px;
    flex-shrink: 0;
  }
  .contact-item--web { color: var(--link-gold); }
</style>
</head>
<body>
<div class="card">
  <div class="brand-mark"></div>
  <div class="brand-name">Roaming<br>Outings</div>
  <div class="tagline">Adventure Riding GPS Trails</div>

  <div class="rider-illustration" role="img" aria-label="Illustration of a rider on a dirt bike mid-jump"></div>

  <div class="contact">
    <div class="contact-name">Keiran Voss</div>
    <ul class="contact-list">
      <li class="contact-item">
        <svg class="contact-icon" viewBox="0 0 30 30" aria-hidden="true">
          <path d="M3 11 Q15 3 27 11 L24 14 L20 12 L20 9 Q15 7 10 9 L10 12 L6 14 Z" fill="var(--icon-grey)"/>
          <rect x="6" y="15" width="18" height="11" rx="2" fill="var(--icon-grey)"/>
        </svg>
        +12 3987 6540
      </li>
      <li class="contact-item">
        <svg class="contact-icon" viewBox="0 0 30 30" aria-hidden="true">
          <rect x="3" y="7" width="24" height="16" fill="none" stroke="var(--icon-grey)" stroke-width="2.2"/>
          <path d="M3 7 L15 17 L27 7" fill="none" stroke="var(--icon-grey)" stroke-width="2.2"/>
        </svg>
        keiran@roamingoutings.com
      </li>
      <li class="contact-item contact-item--web">
        <svg class="contact-icon" viewBox="0 0 30 30" aria-hidden="true">
          <g fill="none" stroke="var(--icon-grey)" stroke-width="1.8">
            <circle cx="15" cy="15" r="12"/>
            <ellipse cx="15" cy="15" rx="5.5" ry="12"/>
            <line x1="3" y1="15" x2="27" y2="15"/>
            <line x1="15" y1="3" x2="15" y2="27"/>
            <path d="M5 9 H25 M5 21 H25"/>
          </g>
        </svg>
        roamingoutings.com.au
      </li>
    </ul>
  </div>
</div>
</body>
</html>
```